Merry Christmas & A Happy New Year

We need a Greeting Card for this year's Christmas & New Year.

We are a company dealing in the Mechanical Engineering & Manufacturing Industry. Example: Aero Space, Oil & Gas, Marine, etc…

• Company Logo

```html
<!DOCTYPE html>
<html lang="en">
<head>
<meta charset="utf-8">
<title>Merry Christmas &amp; A Happy New Year – Greeting Card</title>
<link rel="stylesheet" href="https://fonts.googleapis.com/css2?family=Crimson+Text:wght@400;600&display=swap">
<style>
  :root {
    --backdrop: #ecebe8;
    --burgundy: #6e1028;
    --burgundy-deep: #560a1e;
    --burgundy-glow: #8a1a36;
    --cream: #f6efe4;
    --paper: #fbfaf7;
    --paper-shade: #eeede8;
    --ink: #7a1530;
  }
  * { box-sizing: border-box; margin: 0; padding: 0; }
  html, body {
    width: 1200px;
    height: 701px;
    overflow: hidden;
    background: var(--backdrop);
    font-family: "Crimson Text", Georgia, serif;
  }
  .canvas {
    position: relative;
    width: 1200px;
    height: 701px;
  }

  /* Front cover */
  .card-front {
    position: absolute;
    left: 45px;
    top: 125px;
    width: 350px;
    height: 450px;
    background: radial-gradient(ellipse at 50% 50%, var(--burgundy-glow) 0%, var(--burgundy) 45%, var(--burgundy-deep) 100%);
    box-shadow: 0 6px 18px rgba(0,0,0,0.18);
    text-align: center;
    color: var(--cream);
  }
  .tree-artwork {
    position: absolute;
    left: 92px;
    top: 82px;
    width: 166px;
    height: 208px;
    clip-path: polygon(50% 0, 100% 100%, 0 100%);
    background: linear-gradient(180deg, rgba(246,239,228,0.9) 0%, rgba(246,239,228,0.8) 100%);
  }
  .greeting-title {
    position: absolute;
    left: 0;
    right: 0;
    top: 318px;
    font-size: 27px;
    font-weight: 400;
    letter-spacing: 0.4px;
    line-height: 1;
  }
  .greeting-subtitle {
    position: absolute;
    left: 0;
    right: 0;
    top: 352px;
    display: flex;
    align-items: center;
    justify-content: center;
    gap: 8px;
    font-size: 8px;
    letter-spacing: 2px;
    text-transform: uppercase;
    line-height: 1;
  }
  .greeting-subtitle .rule {
    width: 34px;
    height: 1px;
    background: var(--cream);
    opacity: 0.6;
  }

  /* Inside spread */
  .card-inside {
    position: absolute;
    left: 450px;
    top: 125px;
    width: 700px;
    height: 450px;
    display: flex;
    box-shadow: 0 6px 18px rgba(0,0,0,0.14);
  }
  .panel {
    width: 350px;
    height: 100%;
  }
  .panel-left {
    background: linear-gradient(90deg, var(--paper) 0%, var(--paper-shade) 100%);
  }
  .panel-right {
    background: var(--paper);
    border-left: 1px solid var(--paper-shade);
    text-align: center;
    color: var(--ink);
    padding-top: 118px;
  }
  .message {
    font-size: 14.5px;
    line-height: 26px;
  }
  .signature {
    margin-top: 18px;
    font-size: 14.5px;
    line-height: 26px;
  }
  .company-mark {
    margin-top: 22px;
    display: inline-flex;
    align-items: center;
    gap: 5px;
    font-size: 12px;
    font-weight: 600;
    color: var(--ink);
  }
  .company-mark .dot {
    width: 10px;
    height: 10px;
    border-radius: 50%;
    background: var(--ink);
  }
</style>
</head>
<body>
<main class="canvas">
  <section class="card-front">
    <div class="tree-artwork" role="img" aria-label="Christmas tree built from rows of cream engineering gears"></div>
    <h1 class="greeting-title">Merry Christmas</h1>
    <p class="greeting-subtitle"><span class="rule"></span>&amp; a happy new year<span class="rule"></span></p>
  </section>

  <section class="card-inside">
    <div class="panel panel-left"></div>
    <div class="panel panel-right">
      <p class="message">We wish you Merry Christmas<br>and a healthy, prosperous<br>and happy 2014</p>
      <p class="signature">The Brightgear Works Team</p>
      <div class="company-mark"><span class="dot"></span>Brightgear Works</div>
    </div>
  </section>
</main>
</body>
</html>
```